Harborline Supply Company Business Card Design

The Business Card will be one side only with Harborline Supplies Company Logo
Card should have:
Name
Title
Office phone Number
Cell Number
email address
Website
Street Address
Our Slogan is Sturdy and Steadfast
Looking for something that stands out from other business cards

Target Market(s)

Heavy equipment Lease Company

```html
<!DOCTYPE html>
<html lang="en">
<head>
<meta charset="utf-8">
<title>Harborline Supplies Company – Business Card</title>
<link href="https://fonts.googleapis.com/css2?family=Roboto:wght@400;500;700;900&display=swap" rel="stylesheet">
<style>
  :root {
    --navy: #2e2f7f;
    --red: #d7262e;
    --white: #ffffff;
    --map-grey: #e4e4e8;
    --backdrop: #e9e9ec;
    --ink: #2a2a55;
  }
  * { box-sizing: border-box; margin: 0; padding: 0; }
  html, body { width: 1200px; height: 800px; overflow: hidden; }
  body {
    background: var(--backdrop);
    font-family: "Roboto", Arial, sans-serif;
    position: relative;
  }
  .card {
    position: absolute;
    width: 540px;
    height: 309px;
    background: var(--white);
    box-shadow: 0 6px 22px rgba(0,0,0,0.18);
    overflow: hidden;
  }
  /* ---------- front ---------- */
  .card--front { left: 40px; top: 246px; }
  .front__map {
    position: absolute;
    left: 70px; top: 30px;
    width: 440px; height: 250px;
    background: radial-gradient(closest-side, var(--map-grey) 0%, #efeff2 55%, rgba(255,255,255,0) 100%);
  }
  .front__brand {
    position: absolute;
    left: 0; right: 0; top: 126px;
    display: flex; align-items: center; justify-content: center; gap: 12px;
  }
  .front__mark { width: 22px; height: 22px; background: var(--red); flex: none; }
  .front__name {
    font-weight: 900; font-size: 29px; letter-spacing: 0.5px;
    color: var(--navy); text-transform: uppercase; white-space: nowrap;
  }
  .front__web {
    position: absolute; left: 0; right: 0; top: 174px; text-align: center;
    font-size: 13px; font-weight: 500; letter-spacing: 2.5px; color: var(--navy);
  }
  /* ---------- back ---------- */
  .card--back { left: 620px; top: 246px; }
  .back__top {
    position: absolute; left: 0; top: 0; width: 100%; height: 118px;
    background: var(--navy);
  }
  .back__company {
    position: absolute; left: 30px; top: 16px;
    font-weight: 900; font-size: 33px; color: var(--red);
    text-transform: uppercase; letter-spacing: 0.3px; line-height: 1; white-space: nowrap;
  }
  .back__sub {
    position: absolute; left: 30px; top: 56px; width: 480px;
    display: flex; align-items: center; gap: 10px;
  }
  .back__rule { flex: 1; height: 1px; background: rgba(255,255,255,0.8); }
  .back__sub-word {
    color: var(--white); font-weight: 700; font-size: 20px; letter-spacing: 9px;
  }
  .back__slogan {
    position: absolute; right: 30px; top: 88px;
    color: var(--white); font-size: 13px; letter-spacing: 2.5px; white-space: nowrap;
  }
  .back__line {
    position: absolute; left: 0; width: 100%; height: 2px; background: var(--red);
  }
  .back__line--top { top: 123px; }
  .back__line--bottom { top: 253px; }
  .back__bottom {
    position: absolute; left: 0; top: 259px; width: 100%; height: 50px;
    background: var(--navy);
    display: flex; align-items: center; justify-content: center;
    color: var(--white); font-size: 13.5px; letter-spacing: 0.4px;
  }
  .back__logo {
    position: absolute; left: 30px; top: 174px;
    display: flex; align-items: center; gap: 8px;
  }
  .back__logo-mark { width: 16px; height: 16px; background: var(--red); flex: none; }
  .back__logo-name {
    font-weight: 900; font-size: 22px; color: var(--navy); text-transform: uppercase;
  }
  .back__divider {
    position: absolute; left: 238px; top: 140px; width: 1px; height: 100px;
    background: var(--red); opacity: 0.6;
  }
  .contact { position: absolute; left: 258px; top: 134px; }
  .contact__name { color: var(--red); font-weight: 700; font-size: 19px; line-height: 1.1; }
  .contact__title { color: var(--ink); font-size: 12.5px; margin-bottom: 4px; }
  .contact__row {
    display: flex; align-items: center; gap: 7px;
    color: var(--ink); font-size: 12.5px; line-height: 18px; white-space: nowrap;
  }
  .contact__icon { width: 13px; height: 13px; flex: none; }
</style>
</head>
<body>

  <section class="card card--front" aria-label="Card front">
    <div class="front__map" role="img" aria-label="Faint grey world map in the background"></div>
    <div class="front__brand">
      <span class="front__mark"></span>
      <span class="front__name">Harborline Pumps</span>
    </div>
    <p class="front__web">www.harborlinesupply.com</p>
  </section>

  <section class="card card--back" aria-label="Card back">
    <div class="back__top">
      <h1 class="back__company">Harborline Supplies</h1>
      <div class="back__sub">
        <span class="back__rule"></span>
        <span class="back__sub-word">COMPANY</span>
        <span class="back__rule"></span>
      </div>
      <p class="back__slogan">Sturdy and Steadfast</p>
    </div>
    <div class="back__line back__line--top"></div>

    <div class="back__logo">
      <span class="back__logo-mark"></span>
      <span class="back__logo-name">Harborline</span>
    </div>
    <div class="back__divider"></div>

    <div class="contact">
      <p class="contact__name">Dana Whitfield</p>
      <p class="contact__title">Owner/President</p>
      <p class="contact__row">
        <svg class="contact__icon" viewBox="0 0 14 14"><circle cx="7" cy="7" r="7" fill="#d7262e"/><rect x="5" y="3.5" width="4" height="7" rx="0.8" fill="#fff"/></svg>
        555-010-2233
      </p>
      <p class="contact__row">
        <svg class="contact__icon" viewBox="0 0 14 14"><circle cx="7" cy="7" r="7" fill="#d7262e"/><path d="M4 5.5 Q7 3 10 5.5 L9.2 7 L8 6.4 L6 6.4 L4.8 7 Z M5 7.5 H9 V10.5 H5 Z" fill="#fff"/></svg>
        555-010-4477
      </p>
      <p class="contact__row">
        <svg class="contact__icon" viewBox="0 0 14 14"><circle cx="7" cy="7" r="7" fill="#d7262e"/><rect x="3.5" y="4.5" width="7" height="5" fill="#fff"/><path d="M3.5 4.5 L7 7.3 L10.5 4.5" stroke="#d7262e" stroke-width="0.8" fill="none"/></svg>
        info@harborlinesupply.com
      </p>
      <p class="contact__row">
        <svg class="contact__icon" viewBox="0 0 14 14"><circle cx="7" cy="7" r="7" fill="#d7262e"/><circle cx="7" cy="7" r="3.6" fill="none" stroke="#fff" stroke-width="0.9"/><path d="M3.4 7 H10.6 M7 3.4 V10.6" stroke="#fff" stroke-width="0.8"/></svg>
        www.harborlinesupply.com
      </p>
    </div>

    <div class="back__line back__line--bottom"></div>
    <footer class="back__bottom">PO BOX 480, Dockside Road, 3rd Lane, Arizona 85001</footer>
  </section>

</body>
</html>
```